wine label for ultra premium vineyard in Bendigo, Central Otago, New Zealand

"LARKSPUR" is our new wine brand, with grapes grown in our spectacular "ter Hoeven" vineyard. The small, elevated vineyard overlooks a river valley and snowy mountains. We would like a highly elegant label for our 2018 pinot noir wine, which highlights the quality of wine and our very special vineyard location. "LARKSPUR" has to be prominent, with secondary emphasis on "ter Hoeven vineyard" and "Bendigo, Central Otago". A stylized LARKSPUR logo (bird) could be a useful design device instead of the commonly seen illustrated mountain landscape (which is quite common for our local wines). Label size 90 high, 110 wide. Please use a pinot noir / burgundy bottle. See here for vineyard pics, and also below pics for other local wine labels and pics for inspiration / styles. https://www.instagram.com/jas.ter.hoeven.example/

Target Market(s)

average bottle price for this premium red pinot noir would be aroundUS$40. target market are generally urban professionals aged 25 and older with a high degree of interest in pinot noir wine, and who are familiar with New Zealand pinot noir (ie. already know several brands).

Colors
ed252d

Requirements
Must have
• distinctive label, sophisticated look
Nice to have
• classy white paper stock
Should not have
• label must not get too busy... less but high quality and distinctive is more....

```html
<!DOCTYPE html>
<html lang="en">
<head>
<meta charset="utf-8">
<title>LARKSPUR 2018 Pinot Noir – Wine Label</title>
<link rel="stylesheet" href="https://fonts.googleapis.com/css2?family=Tinos&family=Roboto:wght@200&family=Source+Sans+3:wght@400&display=swap">
<style>
  :root {
    --page-bg: #ffffff;
    --label-paper: #ffffff;
    --label-frame: #2b2b2b;
    --brand-red: #ed252d;
    --ink-grey: #3c3c3e;
    --gold-line: #e2bf2a;
    --gold-pale: #f6ecc2;
    --engraving-grey: #b9b9b9;
  }
  * { margin: 0; padding: 0; box-sizing: border-box; }
  html, body {
    width: 1200px;
    height: 1200px;
    overflow: hidden;
    background: var(--page-bg);
  }
  .canvas {
    position: relative;
    width: 1200px;
    height: 1200px;
  }
  .wine-label {
    position: absolute;
    left: 164px;
    top: 92px;
    width: 872px;
    height: 1017px;
    background: var(--label-paper);
    border: 2px solid var(--label-frame);
  }
  .bird-emblem {
    position: absolute;
    left: 26px;
    top: 46px;
    width: 543px;
    height: 533px;
  }
  .brand-name {
    position: absolute;
    left: 262px;
    top: 452px;
    font-family: "Tinos", "Times New Roman", serif;
    font-variant: small-caps;
    font-size: 125px;
    line-height: 1;
    color: var(--brand-red);
    letter-spacing: 0.01em;
    white-space: nowrap;
  }
  .vintage {
    position: absolute;
    left: 0;
    width: 100%;
    top: 640px;
    text-align: center;
    font-family: "Roboto", "Helvetica Neue", sans-serif;
    font-weight: 200;
    font-size: 146px;
    line-height: 1;
    color: var(--ink-grey);
  }
  .varietal {
    position: absolute;
    left: 0;
    width: 100%;
    top: 800px;
    text-align: center;
    font-family: "Source Sans 3", "Myriad Pro", sans-serif;
    font-size: 45px;
    line-height: 1;
    color: var(--ink-grey);
  }
  .region {
    position: absolute;
    left: 0;
    width: 100%;
    top: 944px;
    text-align: center;
    font-family: "Source Sans 3", "Myriad Pro", sans-serif;
    font-size: 48px;
    line-height: 1;
    color: var(--ink-grey);
  }
</style>
</head>
<body>
  <main class="canvas">
    <section class="wine-label">
      <svg class="bird-emblem" viewBox="0 0 543 533" role="img" aria-label="Gold line drawing of a bird in flight, its body filled with an engraved vineyard landscape with a tree, hills and vine rows">
        <defs>
          <radialGradient id="emblem-tone" cx="45%" cy="55%" r="60%">
            <stop offset="0%" stop-color="var(--engraving-grey)" stop-opacity="0.55"/>
            <stop offset="55%" stop-color="var(--gold-pale)" stop-opacity="0.7"/>
            <stop offset="100%" stop-color="var(--gold-pale)" stop-opacity="0"/>
          </radialGradient>
        </defs>
        <rect x="0" y="0" width="543" height="533" fill="url(#emblem-tone)"/>
      </svg>
      <h1 class="brand-name">Larkspur</h1>
      <p class="vintage">2018</p>
      <p class="varietal">Pinot noir wine</p>
      <p class="region">Bendigo, Central Otago</p>
    </section>
  </main>
</body>
</html>
```